Business Card Design Project

We need a business card designed for a new Luxury Custom Homebuilding company based in Arizona. We previous were called "Belcrest Estates" but want to start using "Belcrest Custom Homes" We want the message to communicate high end, luxury and cutting-edge. We like the blue, white and black color scheme.
Belcrest Custom Homes
Marcus T. Halloway
Chief Executive Officer
Office: 480-555-0142
Mobile: 480-555-0178
email: marc@belcrestcustom-example.com
web adress: www.BelcrestCustom-example.com
Updates
We have made a change to our website address and email address based on recieving feedback from a nmber of individuals. The feedback was web address and email address was to long. Therefore we have made a change. The new web adress and email adress are the following.
www.BelcrestCustom-example.com
marc@belcrestcustom-example.com
Also I decided against using in yellow. I like the colors blue,black, white and maybe gray.
Target Market(s)
Our target market is the wealthy individuals looking for a luxury high-end custom home.
Industry/Entity Type
Business
Look and feel

```html
<!DOCTYPE html>
<html lang="en">
<head>
<meta charset="utf-8">
<title>Belcrest Custom Homes – Business Card</title>
<link rel="stylesheet" href="https://fonts.googleapis.com/css2?family=Source+Sans+3:wght@300;400;700&family=PT+Sans+Narrow&display=swap">
<style>
  :root {
    --page: #ffffff;
    --steel-blue: #3f6486;
    --steel-blue-light: #6b93b8;
    --steel-blue-deep: #1f3147;
    --graphite: #3b3e42;
    --graphite-dark: #232528;
    --band: #0d1014;
    --white: #ffffff;
    --accent-blue: #6ea6dc;
    --caption: #7a7a7a;
    --subtle: #cdd7e2;
  }
  * { box-sizing: border-box; margin: 0; padding: 0; }
  html, body {
    width: 1200px; height: 900px; overflow: hidden;
    background: var(--page);
    font-family: "Source Sans 3", "Myriad Pro", sans-serif;
  }
  .canvas { position: relative; width: 1200px; height: 900px; }

  .card {
    position: absolute;
    width: 631px; height: 362px;
    border-radius: 22px;
    overflow: hidden;
    background: var(--graphite);
    box-shadow: 0 1px 4px rgba(0,0,0,.35);
  }
  .card--front { left: 57px; top: 58px; }
  .card--back  { left: 514px; top: 478px; }

  .card__blue {
    position: absolute; left: 0; top: 0; bottom: 0; width: 316px;
    background:
      radial-gradient(ellipse 60% 55% at 70% 35%, var(--steel-blue-light) 0%, transparent 70%),
      radial-gradient(ellipse 80% 70% at 20% 80%, var(--steel-blue-deep) 0%, transparent 75%),
      var(--steel-blue);
  }
  .card__gray {
    position: absolute; left: 316px; right: 0; top: 0; bottom: 0;
    background:
      radial-gradient(ellipse 70% 60% at 40% 45%, #54585c 0%, transparent 70%),
      radial-gradient(ellipse 70% 60% at 90% 90%, var(--graphite-dark) 0%, transparent 75%),
      var(--graphite);
  }
  .card__band {
    position: absolute; left: 0; right: 0; height: 25px;
    background: linear-gradient(var(--band), #1a2029);
  }
  .card__band--top { top: 0; }
  .card__band--bottom { bottom: 0; height: 23px; background: linear-gradient(#1a2029, var(--band)); }

  .holder { position: absolute; left: 30px; top: 50px; color: var(--white); }
  .holder__name { font-weight: 300; font-size: 28px; letter-spacing: .5px; line-height: 1; }
  .holder__title { font-weight: 400; font-size: 12.5px; color: var(--subtle); margin-top: 8px; }

  .contact { position: absolute; left: 27px; top: 259px; list-style: none; font-size: 14px; line-height: 21px; color: var(--white); }
  .label { color: var(--accent-blue); }

  .website { position: absolute; right: 30px; top: 301px; font-size: 14px; color: var(--white); }

  .brand { position: absolute; color: var(--white); font-weight: 700; text-align: right; line-height: .9; }
  .brand__name { display: block; font-size: 86px; letter-spacing: -2px; }
  .brand__line { display: block; font-size: 40px; text-transform: uppercase; letter-spacing: 0; }
  .card--front .brand { right: 30px; top: 105px; }

  .card--back .brand {
    left: 280px; top: 181px;
    transform: translate(-50%, -50%) rotate(-90deg);
    transform-origin: center;
    white-space: nowrap;
  }
  .card--back .brand__name { font-size: 64px; }
  .card--back .brand__line { font-size: 30px; }

  .back-website {
    position: absolute; left: 588px; top: 181px;
    transform: translate(-50%, -50%) rotate(-90deg);
    white-space: nowrap; font-size: 14px; color: var(--white);
  }
  .back-website strong { font-weight: 700; }
  .back-website .label { font-weight: 700; }

  .caption {
    position: absolute; left: 55px; top: 785px;
    font-family: "PT Sans Narrow", "Arial Narrow", sans-serif;
    font-size: 22px; line-height: 29px; color: var(--caption);
  }
</style>
</head>
<body>
<main class="canvas">

  <section class="card card--front" aria-label="Business card front">
    <div class="card__blue"></div>
    <div class="card__gray"></div>
    <div class="card__band card__band--top"></div>
    <div class="card__band card__band--bottom"></div>

    <div class="holder">
      <p class="holder__name">Marcus T. Halloway</p>
      <p class="holder__title">Chief Executive Officer</p>
    </div>

    <p class="brand">
      <span class="brand__name">Belcrest</span>
      <span class="brand__line">Custom Homes</span>
    </p>

    <ul class="contact">
      <li><span class="label">Office:</span> 480-555-0142</li>
      <li><span class="label">Mobile:</span> 480-555-0178</li>
      <li><span class="label">Email:</span> marc@belcrestcustom-example.com</li>
    </ul>

    <p class="website"><span class="label">Website:</span> www.BelcrestCustom-example.com</p>
  </section>

  <section class="card card--back" aria-label="Business card back">
    <div class="card__blue"></div>
    <div class="card__gray"></div>
    <div class="card__band card__band--top"></div>
    <div class="card__band card__band--bottom"></div>

    <p class="brand">
      <span class="brand__name">Belcrest</span>
      <span class="brand__line">Custom Homes</span>
    </p>

    <p class="back-website">www.<strong>Belcrest</strong><span class="label">Custom</span>-example.com</p>
  </section>

  <p class="caption">Business Card<br>front&amp;back panel</p>

</main>
</body>
</html>
```